Corvane Collective Web Presence Design and Relaunch

Take existing web files and "clean up" for a a more presentable web landing pad.
posted presently on a site pad CSS template. at www.corvanecollective.org

The site is clunky and unprofessional looking. Needs to be toned down so the urgency is conveyed, but not via a burning planet image.

Target Market(s)

Non-profit climate adaptation group targeting local government land management agencies, special districts and private landholders of natural resource properties.

Industry/Entity Type

Environment

Coding

Coded - Design and coding required

Number of Pages Required

4 page

Font styles to use
Serif
Sans Serif

Requirements
Must have
• Include current logos, aspects if content on current site www.corvanecollective.org
• A regional Pacific Northwest Focus (US & Canada). Content speaking to urgency but respectful of cultural diversity and norms. Sustainability themes. Emphasis on action and implementation.
Nice to have
• link to like minded projects. Appear to future generations. Diversity in thematic areas ecological resiliency, energy, food security and infrastructure.

```html
<!DOCTYPE html>
<html lang="en">
<head>
<meta charset="utf-8">
<title>Corvane Collective – Implementing Climate Strategies</title>
<link href="https://fonts.googleapis.com/css2?family=Roboto:wght@300;400;500;700&display=swap" rel="stylesheet">
<style>
:root{
  --green:#4cb316;
  --green-dark:#3a9a0c;
  --green-light:#a6d85a;
  --ink:#2b2b2b;
  --muted:#6d6d6d;
  --page:#f4f4f4;
  --white:#ffffff;
  --footer:#2f2f2f;
  --footer-text:#d8d8d8;
}
*{box-sizing:border-box;margin:0;padding:0}
html,body{width:1200px;height:4180px;overflow:hidden}
body{position:relative;background:var(--page);font-family:'Roboto',sans-serif;color:var(--ink)}
.abs{position:absolute}
a{color:inherit;text-decoration:none}

/* header */
.brand{left:74px;top:30px;width:140px;display:flex;flex-direction:column;align-items:center}
.brand-dot{width:40px;height:40px;border-radius:50%;background:var(--green);margin:0 auto 8px}
.brand-name{font-size:15px;font-weight:500;color:var(--green-dark);line-height:1.1;white-space:nowrap}
.nav{left:428px;top:48px;display:flex;align-items:center;gap:34px;font-size:14px;color:#444}
.nav .active{color:var(--green);font-weight:500;position:relative}
.nav .active::before{content:"";position:absolute;left:0;right:0;top:-14px;height:2px;background:var(--green)}
.btn{display:inline-block;border-radius:22px;font-size:14px;font-weight:500;padding:11px 18px;white-space:nowrap}
.btn-outline{border:2px solid var(--green);color:var(--green)}
.btn-solid{background:var(--green);color:var(--white)}
.nav .btn-solid{margin-left:-24px}

/* hero */
.hero-title{left:89px;top:262px;font-size:58px;font-weight:500;line-height:64px;letter-spacing:.5px;color:var(--ink)}
.hero-copy{left:89px;top:400px;width:530px;font-size:14px;line-height:22.5px;color:#555}
.hero-btn{left:89px;top:510px;padding:12px 20px}
.hero-art{left:478px;top:120px;width:722px;height:510px;border-radius:240px 0 0 60px;background:radial-gradient(ellipse at 60% 60%,#9fd468 0%,#cfe9b7 45%,#eef4ea 75%,transparent 76%)}

/* section titles */
.sec-title{width:1200px;left:0;text-align:center;font-size:40px;font-weight:500;color:var(--ink)}
.sec-title::after{content:"";display:block;width:90px;height:2px;background:var(--green);margin:18px auto 0}

/* featured cards */
.cards{left:89px;top:818px;display:flex;gap:9px}
.card{width:248px;height:282px;background:var(--white);border-radius:6px;box-shadow:0 6px 18px rgba(0,0,0,.08);text-align:center;padding-top:42px}
.card-icon{width:90px;height:90px;border-radius:50%;background:#e6f3da;margin:0 auto;display:flex;align-items:center;justify-content:center}
.card h3{font-size:19px;font-weight:500;margin:28px 0 12px}
.card p{font-size:12px;line-height:16px;color:var(--muted);width:200px;margin:0 auto}

/* about */
.about-art{left:81px;top:1168px;width:552px;height:487px;border-radius:50%;background:radial-gradient(circle at 45% 50%,#8fcf4f,#5fb530 55%,rgba(76,179,22,0) 72%)}
.about-blob{left:363px;top:1172px;width:210px;height:210px;border-radius:50%;background:#e3efd9}
.about{left:688px;top:1252px;width:420px}
.about h2{font-size:42px;font-weight:500;margin-bottom:26px}
.about h4{font-size:20px;font-weight:500;margin-bottom:6px}
.about p{font-size:12px;line-height:18px;color:var(--muted);margin-bottom:28px}

/* stats */
.stats{left:123px;top:1727px;display:flex;gap:80px}
.stat{width:178px}
.stat-circle{width:178px;height:178px;border-radius:50%;background:var(--white);box-shadow:0 8px 18px rgba(0,0,0,.12);display:flex;align-items:center;justify-content:center;font-size:48px;font-weight:500}
.stat-label,.green-label{margin-top:36px;font-size:21px;font-weight:500;display:flex;justify-content:center;white-space:nowrap}

/* green band */
.band{left:0;top:1990px;width:1200px;height:1250px}
.doing{left:86px;top:2188px;color:var(--white)}
.doing h2{font-size:40px;font-weight:700;line-height:50px}
.doing-rule{width:90px;height:2px;background:var(--white);margin:14px 0 32px}
.doing .btn{background:var(--white);color:var(--ink);font-size:14px;padding:11px 20px}
.scene-art{left:487px;top:2092px;width:632px;height:381px;border-radius:30px;background:radial-gradient(ellipse at 50% 50%,rgba(255,255,255,.28) 0%,rgba(255,255,255,.12) 45%,rgba(255,255,255,0) 72%)}
.recent-title{left:0;width:1200px;top:2548px;text-align:center;color:var(--white);font-size:42px;font-weight:700}
.recent-title::after{content:"";display:block;width:90px;height:2px;background:var(--white);margin:12px auto 0}
.work{width:420px;height:256px;border-radius:22px;overflow:hidden;background:var(--white);text-align:center;padding-top:22px}
.work h3{font-size:23px;font-weight:500;position:relative}
.work p{font-size:13px;color:var(--muted);margin-top:6px;position:relative}
.work-art{position:absolute;left:0;right:0;bottom:0;height:170px}

/* think green */
.greens{left:123px;top:3447px;display:flex;gap:80px}
.green-item{width:178px;position:relative}
.green-img{width:178px;height:178px;border-radius:50%}
.badge{position:absolute;right:-28px;top:-20px;width:62px;height:62px;border-radius:50%;background:var(--white);border:2px solid var(--green);color:var(--green);font-size:19px;font-weight:500;display:flex;align-items:center;justify-content:center}

/* footer */
.footer-bg{left:0;top:3770px;width:1200px;height:410px}
.footer-brand{left:123px;top:3900px;width:254px;display:flex;flex-direction:column;align-items:center;color:var(--white)}
.footer-brand .brand-dot{width:90px;height:90px;background:var(--white);margin-bottom:22px}
.footer-brand .brand-name{color:var(--white);font-size:30px;font-weight:400}
.fcol{top:3882px;color:var(--footer-text);font-size:13.5px}
.fcol h4{color:var(--white);font-size:21px;font-weight:500;margin-bottom:18px}
.fcol li{list-style:none;line-height:26.5px}
.social li{display:flex;align-items:center;gap:14px;line-height:32px}
.sdot{width:22px;height:22px;border-radius:50%;background:#4a4a4a}
.contact li{display:flex;gap:16px;margin-bottom:10px;line-height:19px}
.cicon{width:28px;height:28px;border-radius:50%;background:#4a4a4a;flex:none;display:flex;align-items:center;justify-content:center}
.contact b{color:var(--white);font-weight:500;display:block}
.footer-rule{left:89px;top:4128px;width:1022px;height:1px;background:#474747}
.copyright{left:0;width:1200px;top:4148px;text-align:center;color:var(--footer-text);font-size:13.5px}
</style>
</head>
<body>

<!-- header -->
<div class="abs brand"><div class="brand-dot"></div><div class="brand-name">Corvane Collective</div></div>
<nav class="abs nav">
  <a class="active" href="#">HOME</a>
  <a href="#">About Us</a>
  <a href="#">Causes</a>
  <a href="#">Testimonial</a>
  <a href="#">Events</a>
  <a class="btn btn-outline" href="#">Contact Now</a>
  <a class="btn btn-solid" href="#">Join Us Today</a>
</nav>

<!-- hero -->
<svg class="abs" style="left:0;top:110px" width="500" height="600" aria-hidden="true">
  <circle cx="385" cy="95" r="100" fill="#e5efdc"/>
  <circle cx="55" cy="245" r="42" fill="#e1efd5"/>
  <circle cx="-60" cy="520" r="80" fill="#e6eee0"/>
</svg>
<div class="abs hero-art" role="img" aria-label="Illustration of a green landscape with trees, wind and solar power, a factory and electric cars"></div>
<h1 class="abs hero-title">IMPLEMENTING<br>CLIMATE STRATEGIES</h1>
<p class="abs hero-copy">Dedicated to taking action the Corvane Collective was created to help bring adaptation strategies to life. Working with local communities we are committed to implementing strategies that will sustain communities throughout the Pacific Northwest for generations to come.</p>
<a class="abs btn btn-solid hero-btn" href="#">Contact Us</a>

<!-- featured -->
<svg class="abs" style="left:0;top:760px" width="1200" height="400" aria-hidden="true">
  <path d="M0 200 C150 230 250 60 520 80 C760 100 850 0 1000 0 C1100 0 1160 40 1200 60 L1200 400 L0 400Z" fill="#ffffff"/>
</svg>
<h2 class="abs sec-title" style="top:714px">Featured Projects</h2>
<div class="abs cards">
  <div class="card"><div class="card-icon"><svg width="46" height="46" viewBox="0 0 46 46" fill="none" stroke="#4cb316" stroke-width="2"><circle cx="23" cy="23" r="14"/><path d="M15 23h16M23 15v16"/></svg></div><h3>Adaptation Plans</h3><p>Communities throughout the region have adopted plans to address our changing climate...</p></div>
  <div class="card"><div class="card-icon"><svg width="46" height="46" viewBox="0 0 46 46" fill="none" stroke="#4cb316" stroke-width="2"><path d="M8 34h30M14 34V24M23 34V16M32 34V24"/></svg></div><h3>On The ground...</h3><p>The Collective is familiar &amp; growing throughout the region. Presently our work has us...</p></div>
  <div class="card"><div class="card-icon"><svg width="46" height="46" viewBox="0 0 46 46" fill="none" stroke="#4cb316" stroke-width="2"><path d="M8 30h14l10 6 8-4M23 26c0-8 6-14 14-14 0 8-6 14-14 14z"/></svg></div><h3>Ecological Resilience</h3><p>To endure change Communities need to keep their watersheds functioning...</p></div>
  <div class="card"><div class="card-icon"><svg width="46" height="46" viewBox="0 0 46 46" fill="none" stroke="#4cb316" stroke-width="2"><circle cx="20" cy="23" r="13"/><path d="M30 34c-4-6 2-10 4-16 4 6 6 12-4 16z"/></svg></div><h3>Energy and Food</h3><p>Security of community food &amp; energy have, &amp; always will be, an essential...</p></div>
</div>

<!-- about -->
<div class="abs about-blob"></div>
<div class="abs about-art" role="img" aria-label="Illustration of a leaf-shaped region with towns, wind turbines, forests and a bay"></div>
<svg class="abs" style="left:530px;top:1590px" width="70" height="70" aria-hidden="true"><circle cx="32" cy="32" r="30" fill="#e3efd9"/></svg>
<div class="abs about">
  <h2>About Us</h2>
  <h4>Our History</h4>
  <p>Founded in 2019, the Corvane Collective draws from decades of commitment &amp; action. A core group of committed professionals and community leaders</p>
  <h4>Our Vision</h4>
  <p>We are hyper focused on IMPLEMENTATION. We are eager to get about the business of preparing communities in the Pacific Northwest for fundamen-</p>
  <h4>Our Future</h4>
  <p>The Collective is about community. It is also about dedication to future generations rather than personal gain. We welcome people of all walks of</p>
</div>

<!-- stats -->
<div class="abs stats">
  <div class="stat"><div class="stat-circle">250+</div><div class="stat-label">Project Completed</div></div>
  <div class="stat"><div class="stat-circle">300+</div><div class="stat-label">Donations</div></div>
  <div class="stat"><div class="stat-circle">17+</div><div class="stat-label">Communities Engaged</div></div>
  <div class="stat"><div class="stat-circle">70+</div><div class="stat-label">Volunteers</div></div>
</div>

<!-- green band -->
<svg class="abs band" viewBox="0 0 1200 1250" aria-hidden="true">
  <defs>
    <linearGradient id="bandFill" x1="0" y1="0" x2="0" y2="1">
      <stop offset="0" stop-color="#5cc21c"/>
      <stop offset="1" stop-color="#46a812"/>
    </linearGradient>
  </defs>
  <path d="M0 80 C120 -20 280 10 380 130 C460 230 560 160 700 120 C880 70 1050 110 1200 150 L1200 820 C1130 1000 1050 1000 1000 1000 L600 1000 C540 1000 520 1240 340 1240 C200 1240 120 1180 0 1100Z" fill="url(#bandFill)"/>
</svg>
<div class="abs doing">
  <h2>What<br>We Are Doing ?</h2>
  <div class="doing-rule"></div>
  <a class="btn" href="#">Can You Know This</a>
</div>
<div class="abs scene-art" role="img" aria-label="Illustration of a floating island with two solar-roofed houses, trees, cars and a sun"></div>
<h2 class="abs recent-title">Recent Work</h2>

<div class="abs work" style="left:146px;top:2639px">
  <div class="work-art" role="img" aria-label="Illustration of a globe light bulb beside wind turbines" style="background:linear-gradient(180deg,#fff 0%,#fdf4d6 50%,#f3d26a 100%)"></div>
  <h3>Energy</h3><p>Investing in clean energy</p>
</div>
<div class="abs work" style="left:616px;top:2639px">
  <div class="work-art" role="img" aria-label="Illustration of farmers harvesting vegetables in green fields" style="background:linear-gradient(180deg,#fff 0%,#e9f2df 50%,#a8cf7c 100%)"></div>
  <h3>Food Security</h3><p>Retooling agriculture/span&gt;</p>
</div>
<div class="abs work" style="left:146px;top:2949px">
  <div class="work-art" role="img" aria-label="Illustration of a green city skyline with trees and wind turbines" style="background:linear-gradient(180deg,#fff 0%,#e1f0f8 50%,#a9d5b0 100%)"></div>
  <h3>Ecological Resilience</h3><p>Environmental Progress</p>
</div>
<div class="abs work" style="left:616px;top:2949px;background:linear-gradient(180deg,#b9d9ec,#f3e4c9)">
  <div class="work-art" role="img" aria-label="Illustration of a highway leading to a city skyline" style="background:linear-gradient(180deg,rgba(243,228,201,0) 0%,#e8cfa8 60%,#b9aea2 100%)"></div>
  <h3>Infrastructure</h3><p>Lorem Ipsum has been the industry's</p>
</div>

<!-- think green -->
<h2 class="abs sec-title" style="top:3310px">Think Green! Save Money</h2>
<div class="abs greens">
  <div class="green-item"><div class="green-img" role="img" aria-label="Photo of a clear water splash" style="background:radial-gradient(circle at 40% 40%,#e6f6fc,#7cc7e6 60%,#2f8fbf)"></div><div class="badge">98%</div><div class="green-label">Clean Water</div></div>
  <div class="green-item"><div class="green-img" role="img" aria-label="Photo of a firefighter spraying water on a forest fire" style="background:radial-gradient(circle at 35% 45%,#f4a340,#a54a1c 55%,#2b2f3c)"></div><div class="badge">56%</div><div class="green-label">Forest Rescue</div></div>
  <div class="green-item"><div class="green-img" role="img" aria-label="Photo of a young tree with bright green leaves" style="background:radial-gradient(circle at 50% 40%,#c8ec5a,#5fb62c 55%,#1f7a3a)"></div><div class="badge">77%</div><div class="green-label">Agriculture</div></div>
  <div class="green-item"><div class="green-img" role="img" aria-label="Photo of hands holding a globe with solar panels and wind turbines" style="background:radial-gradient(circle at 50% 45%,#8fd3f0,#4aa84a 55%,#2f6f8f)"></div><div class="badge">84%</div><div class="green-label">Alternative Energy</div></div>
</div>

<!-- footer -->
<svg class="abs footer-bg" viewBox="0 0 1200 410" aria-hidden="true">
  <path d="M0 80 C300 -20 900 -20 1200 80 L1200 410 L0 410Z" fill="#2f2f2f"/>
</svg>
<div class="abs footer-brand"><div class="brand-dot"></div><div class="brand-name">Corvane Collective</div></div>
<div class="abs fcol" style="left:451px">
  <h4>Links</h4>
  <ul><li>Home</li><li>About Us</li><li>Causes</li><li>Testimonial</li><li>Events</li><li>Contact Us</li></ul>
</div>
<div class="abs fcol social" style="left:613px">
  <h4>Follow US</h4>
  <ul><li><span class="sdot"></span>Leafnet</li><li><span class="sdot"></span>Chirper</li><li><span class="sdot"></span>Searchly</li><li><span class="sdot"></span>Streamly</li><li><span class="sdot"></span>RSS</li></ul>
</div>
<div class="abs fcol contact" style="left:798px;width:300px">
  <h4>Contact Info</h4>
  <ul>
    <li><span class="cicon"><svg width="14" height="14" viewBox="0 0 24 24" fill="#fff"><path d="M6.6 10.8a15 15 0 006.6 6.6l2.2-2.2c.3-.3.7-.4 1-.2 1.1.4 2.3.6 3.6.6.6 0 1 .4 1 1V20c0 .6-.4 1-1 1A17 17 0 013 4c0-.6.4-1 1-1h3.5c.6 0 1 .4 1 1 0 1.3.2 2.5.6 3.6.1.3 0 .7-.2 1z"/></svg></span><div><b>Phone</b>555-014-2290</div></li>
    <li><span class="cicon"><svg width="14" height="14" viewBox="0 0 24 24" fill="none" stroke="#fff" stroke-width="2"><path d="M3 5h18v14H3z"/><path d="M3 5l9 8 9-8"/></svg></span><div><b>Email:</b>555-014-2290</div></li>
    <li><span class="cicon"><svg width="14" height="14" viewBox="0 0 24 24" fill="#fff"><path d="M12 2a7 7 0 00-7 7c0 5 7 13 7 13s7-8 7-13a7 7 0 00-7-7zm0 9.5A2.5 2.5 0 1112 6.5a2.5 2.5 0 010 5z"/></svg></span><div><b>Location:</b>418 Alder Row, Bellwick<br>WA 98000</div></li>
  </ul>
</div>
<div class="abs footer-rule"></div>
<div class="abs copyright">Copyright 2020 - All right Reserved.</div>

</body>
</html>
```